Cover for a Series of 5 Poetry Books where there is only a subtle (colour?) change for each

I have 5 poetry books to publish all have the main title of Tides Within My Heart then have different subtitles, which are Lone Voyage Past the Coral Straits; Lone Voyage Across Amber Waters, and 3 others I have yet to determine. I have already published the first one and will attach the cover, which needs re-doing for a reprint. I have been given permission to use a photograph of the moon and a universe star pic as I like the idea of using the moon, as it dominates the tides, oceans and weather systems. I like the thought of using the stars because I love to watch them out at sea and the first design of the book I really love, except that I don't have it in 30dpi which is a must. the photo of the boat on the front is a photo of my boat, and I would like to use it too if possible. all that said I am up for some new ideas that you come up with. my poetry is pretty raw at times, but can also be inspiring and I think the book cover needs to reflect this. I am a solo sailor so it has to reflect that too!
I would like the series of 5 books to have covers that are easily recognisable as a series but also are such that people want to pick them up and read. Maybe change the colour of the moon?
I will have a series of 5 books in paperback and e-books printed 6'x9' with approx 116 to 130 pages max I have the back cover info, the photo of the boat and photo of the author. I can get the barcode for the ISBN numbers. I am self-publishing so I do not have a heap of money!
I have had a couple of folk who have kindly reproduced what I already had, that is not what I am looking for. If I am still not clear, please do drop me a line. I am very new to this process.
Thanks
Target Market(s)
Male and female 15 to 35 and 65 to 85
Requirements
Must have
- 5 covers which are clearly slightly different, but recognisable as a series
Should not have
- unhelpful comments - thanks

```html
<!DOCTYPE html>
<html lang="en">
<head>
<meta charset="utf-8">
<title>Tides Within My Heart — Series Covers</title>
<link rel="stylesheet" href="https://fonts.googleapis.com/css2?family=Great+Vibes&display=swap">
<style>
  :root {
    --sky-deep: #04051a;
    --sky-mid: #171a40;
    --sea-dark: #030202;
    --title-ink: #ffffff;
    --title-shadow: rgba(70, 15, 0, 0.8);
    --gap: #ffffff;
  }
  html, body {
    margin: 0;
    padding: 0;
    width: 1200px;
    height: 360px;
    overflow: hidden;
    background: var(--gap);
  }
  .series {
    display: flex;
    gap: 5px;
    width: 1200px;
    height: 360px;
  }
  .cover {
    position: relative;
    width: 236px;
    height: 360px;
    overflow: hidden;
    background: var(--sky-deep);
  }
  .cover--1 { --moon-light: #f7bd4a; --moon-core: #ec8a30; --moon-edge: #d85a2a; }
  .cover--2 { --moon-light: #f3ad3e; --moon-core: #e8742e; --moon-edge: #d44c2b; }
  .cover--3 { --moon-light: #f1a73d; --moon-core: #e66c2e; --moon-edge: #d2462c; }
  .cover--4 { --moon-light: #efa03a; --moon-core: #e1602f; --moon-edge: #cd3e2d; }
  .cover--5 { --moon-light: #f0a43c; --moon-core: #e3652f; --moon-edge: #cf422c; }

  .cover__scene {
    position: absolute;
    inset: 0;
    width: 236px;
    height: 360px;
    display: block;
  }
  .cover__title {
    position: absolute;
    left: 0;
    right: 0;
    top: 26px;
    margin: 0;
    font-family: "Great Vibes", cursive;
    font-weight: 400;
    font-size: 36px;
    line-height: 62px;
    word-spacing: 8px;
    color: var(--title-ink);
    text-align: center;
    white-space: nowrap;
    text-shadow: 1px 2px 3px var(--title-shadow);
  }
  .cover__title-line { display: block; }
  .cover__title-line--second { padding-left: 14px; }
  .cover__subtitle {
    position: absolute;
    left: 0;
    right: 0;
    top: 220px;
    margin: 0;
    font-family: "Great Vibes", cursive;
    font-size: 12px;
    word-spacing: 2px;
    color: var(--title-ink);
    text-align: center;
    white-space: nowrap;
    text-shadow: 0 0 3px var(--title-shadow), 1px 1px 2px #000;
  }
</style>
</head>
<body>
<main class="series">

  <article class="cover cover--1">
    <svg class="cover__scene" viewBox="0 0 236 360" role="img" aria-label="Photograph of a large amber full moon rising over a calm sea in a starry night sky, with the silhouette of a lone sailing boat and its glowing reflection on the water">
      <defs>
        <radialGradient id="sky-1" cx="50%" cy="40%" r="75%">
          <stop offset="0%" style="stop-color:var(--sky-mid)"/>
          <stop offset="100%" style="stop-color:var(--sky-deep)"/>
        </radialGradient>
        <radialGradient id="moon-1" cx="55%" cy="50%" r="55%">
          <stop offset="0%" style="stop-color:var(--moon-light)"/>
          <stop offset="65%" style="stop-color:var(--moon-core)"/>
          <stop offset="100%" style="stop-color:var(--moon-edge)"/>
        </radialGradient>
        <radialGradient id="glow-1" cx="50%" cy="0%" r="100%">
          <stop offset="0%" style="stop-color:var(--moon-light)"/>
          <stop offset="45%" style="stop-color:var(--moon-core)"/>
          <stop offset="100%" style="stop-color:var(--sea-dark)"/>
        </radialGradient>
      </defs>
      <rect width="236" height="360" fill="url(#sky-1)"/>
      <circle cx="118" cy="148" r="134" fill="url(#moon-1)"/>
      <rect y="272" width="236" height="88" fill="var(--sea-dark)"/>
      <ellipse cx="118" cy="272" rx="128" ry="88" fill="url(#glow-1)"/>
    </svg>
    <h1 class="cover__title"><span class="cover__title-line">Tides Within</span><span class="cover__title-line cover__title-line--second">My Heart</span></h1>
    <p class="cover__subtitle">Lone Voyage Past the Coral Straits</p>
  </article>

  <article class="cover cover--2">
    <svg class="cover__scene" viewBox="0 0 236 360" role="img" aria-label="Photograph of a large red-orange full moon over a calm sea in a starry night sky, with the silhouette of a lone sailing boat and its glowing reflection on the water">
      <defs>
        <radialGradient id="sky-2" cx="50%" cy="40%" r="75%">
          <stop offset="0%" style="stop-color:var(--sky-mid)"/>
          <stop offset="100%" style="stop-color:var(--sky-deep)"/>
        </radialGradient>
        <radialGradient id="moon-2" cx="55%" cy="50%" r="55%">
          <stop offset="0%" style="stop-color:var(--moon-light)"/>
          <stop offset="65%" style="stop-color:var(--moon-core)"/>
          <stop offset="100%" style="stop-color:var(--moon-edge)"/>
        </radialGradient>
        <radialGradient id="glow-2" cx="50%" cy="0%" r="100%">
          <stop offset="0%" style="stop-color:var(--moon-light)"/>
          <stop offset="45%" style="stop-color:var(--moon-core)"/>
          <stop offset="100%" style="stop-color:var(--sea-dark)"/>
        </radialGradient>
      </defs>
      <rect width="236" height="360" fill="url(#sky-2)"/>
      <circle cx="118" cy="148" r="134" fill="url(#moon-2)"/>
      <rect y="272" width="236" height="88" fill="var(--sea-dark)"/>
      <ellipse cx="118" cy="272" rx="128" ry="88" fill="url(#glow-2)"/>
    </svg>
    <h1 class="cover__title"><span class="cover__title-line">Tides Within</span><span class="cover__title-line cover__title-line--second">My Heart</span></h1>
    <p class="cover__subtitle">Lone Voyage Across Amber Waters</p>
  </article>

  <article class="cover cover--3">
    <svg class="cover__scene" viewBox="0 0 236 360" role="img" aria-label="Photograph of a large red-orange full moon over a calm sea in a starry night sky, with the silhouette of a lone sailing boat and its glowing reflection on the water">
      <defs>
        <radialGradient id="sky-3" cx="50%" cy="40%" r="75%">
          <stop offset="0%" style="stop-color:var(--sky-mid)"/>
          <stop offset="100%" style="stop-color:var(--sky-deep)"/>
        </radialGradient>
        <radialGradient id="moon-3" cx="55%" cy="50%" r="55%">
          <stop offset="0%" style="stop-color:var(--moon-light)"/>
          <stop offset="65%" style="stop-color:var(--moon-core)"/>
          <stop offset="100%" style="stop-color:var(--moon-edge)"/>
        </radialGradient>
        <radialGradient id="glow-3" cx="50%" cy="0%" r="100%">
          <stop offset="0%" style="stop-color:var(--moon-light)"/>
          <stop offset="45%" style="stop-color:var(--moon-core)"/>
          <stop offset="100%" style="stop-color:var(--sea-dark)"/>
        </radialGradient>
      </defs>
      <rect width="236" height="360" fill="url(#sky-3)"/>
      <circle cx="118" cy="148" r="134" fill="url(#moon-3)"/>
      <rect y="272" width="236" height="88" fill="var(--sea-dark)"/>
      <ellipse cx="118" cy="272" rx="128" ry="88" fill="url(#glow-3)"/>
    </svg>
    <h1 class="cover__title"><span class="cover__title-line">Tides Within</span><span class="cover__title-line cover__title-line--second">My Heart</span></h1>
    <p class="cover__subtitle">Lone Voyage Across Amber Waters</p>
  </article>

  <article class="cover cover--4">
    <svg class="cover__scene" viewBox="0 0 236 360" role="img" aria-label="Photograph of a large deep red full moon over a calm sea in a starry night sky, with the silhouette of a lone sailing boat and its glowing reflection on the water">
      <defs>
        <radialGradient id="sky-4" cx="50%" cy="40%" r="75%">
          <stop offset="0%" style="stop-color:var(--sky-mid)"/>
          <stop offset="100%" style="stop-color:var(--sky-deep)"/>
        </radialGradient>
        <radialGradient id="moon-4" cx="55%" cy="50%" r="55%">
          <stop offset="0%" style="stop-color:var(--moon-light)"/>
          <stop offset="65%" style="stop-color:var(--moon-core)"/>
          <stop offset="100%" style="stop-color:var(--moon-edge)"/>
        </radialGradient>
        <radialGradient id="glow-4" cx="50%" cy="0%" r="100%">
          <stop offset="0%" style="stop-color:var(--moon-light)"/>
          <stop offset="45%" style="stop-color:var(--moon-core)"/>
          <stop offset="100%" style="stop-color:var(--sea-dark)"/>
        </radialGradient>
      </defs>
      <rect width="236" height="360" fill="url(#sky-4)"/>
      <circle cx="118" cy="148" r="134" fill="url(#moon-4)"/>
      <rect y="272" width="236" height="88" fill="var(--sea-dark)"/>
      <ellipse cx="118" cy="272" rx="128" ry="88" fill="url(#glow-4)"/>
    </svg>
    <h1 class="cover__title"><span class="cover__title-line">Tides Within</span><span class="cover__title-line cover__title-line--second">My Heart</span></h1>
  </article>

  <article class="cover cover--5">
    <svg class="cover__scene" viewBox="0 0 236 360" role="img" aria-label="Photograph of a large deep red full moon over a calm sea in a starry night sky, with the silhouette of a lone sailing boat and its glowing reflection on the water">
      <defs>
        <radialGradient id="sky-5" cx="50%" cy="40%" r="75%">
          <stop offset="0%" style="stop-color:var(--sky-mid)"/>
          <stop offset="100%" style="stop-color:var(--sky-deep)"/>
        </radialGradient>
        <radialGradient id="moon-5" cx="55%" cy="50%" r="55%">
          <stop offset="0%" style="stop-color:var(--moon-light)"/>
          <stop offset="65%" style="stop-color:var(--moon-core)"/>
          <stop offset="100%" style="stop-color:var(--moon-edge)"/>
        </radialGradient>
        <radialGradient id="glow-5" cx="50%" cy="0%" r="100%">
          <stop offset="0%" style="stop-color:var(--moon-light)"/>
          <stop offset="45%" style="stop-color:var(--moon-core)"/>
          <stop offset="100%" style="stop-color:var(--sea-dark)"/>
        </radialGradient>
      </defs>
      <rect width="236" height="360" fill="url(#sky-5)"/>
      <circle cx="118" cy="148" r="134" fill="url(#moon-5)"/>
      <rect y="272" width="236" height="88" fill="var(--sea-dark)"/>
      <ellipse cx="118" cy="272" rx="128" ry="88" fill="url(#glow-5)"/>
    </svg>
    <h1 class="cover__title"><span class="cover__title-line">Tides Within</span><span class="cover__title-line cover__title-line--second">My Heart</span></h1>
  </article>

</main>
</body>
</html>
```